QUORVANTIX Process Banner

I am looking to make an ~82" x 32" stand up vertical banner that includes our companies core values, process and service delivery. I would like to be able to take these different areas and use them in other signage and print materials as well. I have attached examples of what we are looking for along with what content we already have. The content we have is very basic. Looking for some better design and creativity on how to display our core values, process and service delivery

Core Values = Do the right thing, Service Driven, Innovative, All In

Delivery Areas = Service Delivery, Centralized Services, Strategy, Automation, Technology Alignment

Our process: assessment (find a fit), proposal, onboarding, IT Roadmap, ongoing support, monitoring, maintenance

```html
<!DOCTYPE html>
<html lang="en">
<head>
<meta charset="UTF-8">
<title>QUORVANTIX Process Banner</title>
<link rel="stylesheet" href="https://fonts.googleapis.com/css2?family=Roboto+Condensed:wght@400;700;800&display=swap">
<style>
  :root {
    --stage: #fdf0df;
    --banner: #fafafa;
    --orange: #f7941d;
    --orange-deep: #ee5a2a;
    --ink: #111111;
    --line: #222222;
    --strip: #dedede;
    --pattern-light: #f5f5f5;
    --pattern-dark: #e4e4e4;
    --flow-fill: #ececec;
  }
  * { margin: 0; padding: 0; box-sizing: border-box; }
  html, body {
    width: 1200px; height: 1200px; overflow: hidden;
    background: var(--stage);
    font-family: "Roboto Condensed", "Arial Narrow", sans-serif;
    color: var(--ink);
  }
  .banner {
    position: absolute; left: 395px; top: 74px;
    width: 411px; height: 1051px;
    background: var(--banner);
    overflow: hidden;
  }
  .top-band {
    position: absolute; left: 0; top: 0; width: 100%; height: 31px;
    background: linear-gradient(90deg, var(--orange-deep), var(--orange));
  }
  .texture {
    position: absolute; left: 0; top: 526px; width: 100%; height: 525px;
    background: linear-gradient(180deg, var(--banner) 0%, var(--pattern-light) 30%, var(--pattern-dark) 100%);
  }
  .connectors { position: absolute; left: 0; top: 0; }
  .value {
    position: absolute; width: 89px; height: 89px;
    border: 1.5px dotted var(--line);
    background: var(--banner);
    display: flex; align-items: center; justify-content: center;
    text-align: center; font-weight: 700; font-size: 15px; line-height: 1.3;
  }
  .value--top { left: 160px; top: 84px; }
  .value--left { left: 36px; top: 208px; }
  .value--right { left: 286px; top: 208px; }
  .value--bottom { left: 160px; top: 333px; }
  .core {
    position: absolute; left: 145px; top: 193px; width: 119px; height: 118px;
    border-radius: 11px;
    background: linear-gradient(90deg, var(--orange-deep) 0%, var(--orange) 12%, var(--orange) 100%);
    display: flex; flex-direction: column; align-items: center; justify-content: center;
    font-weight: 700; line-height: 1;
  }
  .core__main { font-size: 26px; }
  .core__sub { font-size: 17px; margin-top: 3px; }
  .delivery-title {
    position: absolute; left: 185px; top: 496px;
    font-size: 34px; font-weight: 700; line-height: 1;
  }
  .delivery-strip {
    position: absolute; left: 150px; top: 539px; width: 11px; height: 197px;
    background: var(--strip);
  }
  .delivery-list {
    position: absolute; left: 161px; top: 539px; width: 250px; height: 197px;
    background: var(--orange);
    list-style: none; padding: 9px 0 0 29px;
  }
  .delivery-list li {
    font-size: 15px; font-weight: 700; line-height: 36.5px; height: 36.5px;
  }
  .flow-graphic {
    position: absolute; left: 42px; top: 557px; width: 75px; height: 159px;
    background: var(--flow-fill);
  }
  .process {
    position: absolute; left: 0; top: 812px; width: 100%;
    text-align: center;
  }
  .process__title { font-size: 39px; font-weight: 700; line-height: 1.1; }
  .process__steps { font-size: 25px; font-weight: 400; line-height: 31px; }
</style>
</head>
<body>
  <div class="banner">
    <div class="top-band"></div>
    <div class="texture" role="img" aria-label="Soft grey diamond tile pattern"></div>

    <svg class="connectors" width="411" height="430" viewBox="0 0 411 430">
      <g stroke="#222" stroke-width="1.5" stroke-dasharray="2 3" fill="none">
        <line x1="204.5" y1="173" x2="204.5" y2="193"/>
        <line x1="204.5" y1="311" x2="204.5" y2="333"/>
        <line x1="125" y1="252" x2="145" y2="252"/>
        <line x1="264" y1="252" x2="286" y2="252"/>
      </g>
    </svg>

    <div class="value value--top">Do the<br>right thing</div>
    <div class="value value--left">Service<br>Driven</div>
    <div class="value value--right">Innovative</div>
    <div class="value value--bottom">All In</div>
    <div class="core"><span class="core__main">CORE</span><span class="core__sub">VALUES</span></div>

    <h2 class="delivery-title">Delivery Areas</h2>
    <div class="flow-graphic" role="img" aria-label="Zigzag arrow path illustration showing a stepwise flow"></div>
    <div class="delivery-strip"></div>
    <ul class="delivery-list">
      <li>Service Delivery</li>
      <li>Centralized Services</li>
      <li>Strategy</li>
      <li>Automation</li>
      <li>Technology Alignment</li>
    </ul>

    <div class="process">
      <h2 class="process__title">Our process:</h2>
      <p class="process__steps">assessment (find a fit),<br>proposal, onboarding,<br>IT Roadmap, ongoing support,<br>monitoring, maintenance</p>
    </div>
  </div>
</body>
</html>
```